Podcast Cover Art for Fast Growing Show (Ill include a gracious tip!)

This artwork is for "The Steadfast Fellow Show." The podcast is for men, and it's all about self-improvement, confidence, success, money, women and masculinity. It's for the guy who wants to improve himself. I'd like for my picture to be included — in black and white — and I want the text to read: "The Steadfast Fellow Show" and somewhere in there it'll say: "with Dale Prowen." I'm open to color schemes. The podcast is a little edgy so I'd like for that to be represented in the design. Thank you! (((Here's the podcast page if you wanna check it out: http://steadfastfellowshow.castorbit.net/)))

Target Market(s)

Men who want to attract women and improve their lives!

Font styles to use
Serif

Colors

Designer to choose colors to be used in the design.

Requirements
Must have
• My image in it (in black and white) and the two titles: "The Steadfast Fellow Show" and "with Dale Prowen"
Nice to have
• My logo in it somehow (which is the arrow looking logo attached below). I've also found that my image looks best in black and white and with a circular type cut out (although I'm open to different design ideas). I've attached my logo with a circular cut out below so you can see what I'm talking about.
Should not have
• Flowers. Teddy bears. ice cream.

```html
<!DOCTYPE html>
<html lang="en">
<head>
<meta charset="utf-8">
<title>The Steadfast Fellow Show — Cover Art</title>
<link rel="stylesheet" href="https://fonts.googleapis.com/css2?family=Marcellus+SC&family=Montserrat:wght@400;600&family=Great+Vibes&display=swap">
<style>
  :root {
    --red: #e4222b;
    --black: #000000;
    --white: #ffffff;
    --ring: #1a1a1a;
    --photo-light: #e8e8e8;
    --photo-dark: #3a3a3a;
  }
  html, body {
    margin: 0;
    padding: 0;
    overflow: hidden;
    background: var(--black);
  }
  .cover {
    position: relative;
    width: 1191px;
    height: 1200px;
    overflow: hidden;
    background: var(--black);
  }
  .backdrop {
    position: absolute;
    inset: 0;
  }
  .show-title {
    position: absolute;
    left: 40px;
    top: 36px;
    margin: 0;
    font-family: "Marcellus SC", serif;
    font-weight: 400;
    font-size: 90px;
    line-height: 156px;
    color: var(--white);
    z-index: 2;
  }
  .show-title span { display: block; }
  .show-label {
    position: absolute;
    left: 790px;
    top: 282px;
    font-family: "Montserrat", sans-serif;
    font-weight: 600;
    font-size: 50px;
    letter-spacing: 22px;
    color: var(--white);
  }
  .brand-name {
    position: absolute;
    left: 930px;
    top: 90px;
    width: 190px;
    text-align: center;
    font-family: "Marcellus SC", serif;
    font-size: 34px;
    line-height: 44px;
    color: var(--black);
  }
  .host-photo {
    position: absolute;
    left: 311px;
    top: 320px;
    width: 570px;
    height: 570px;
    border-radius: 50%;
    background: radial-gradient(circle at 50% 40%, var(--photo-light) 0%, #bdbdbd 45%, var(--photo-dark) 100%);
    box-shadow: 0 0 0 16px var(--ring);
  }
  .host-with {
    position: absolute;
    left: 0;
    width: 1191px;
    top: 948px;
    text-align: center;
    font-family: "Montserrat", sans-serif;
    font-size: 38px;
    color: var(--white);
  }
  .host-name {
    position: absolute;
    left: 0;
    width: 1191px;
    top: 1000px;
    text-align: center;
    font-family: "Great Vibes", cursive;
    font-size: 92px;
    line-height: 1;
    color: var(--white);
  }
</style>
</head>
<body>
<main class="cover">
  <svg class="backdrop" width="1191" height="1200" viewBox="0 0 1191 1200" aria-hidden="true">
    <rect width="1191" height="1200" fill="var(--black)"/>
    <path fill="var(--red)" d="M0 0 H1191 V612 L1140 616 L1080 611 L1010 618 L950 613 L880 620 L700 616 L400 618 L300 622 L240 619 L160 626 L110 630 L70 640 L60 660 L48 668 L40 640 L30 624 L0 620 Z"/>
    <path fill="var(--red)" d="M40 608 L140 612 L60 618 Z M20 660 L70 655 L55 666 Z M890 628 L1010 622 L930 634 Z M900 640 L980 636 L920 644 Z M1000 616 L1130 612 L1040 620 Z"/>
  </svg>

  <h1 class="show-title">
    <span>The</span>
    <span>Steadfast</span>
    <span>Fellow</span>
  </h1>
  <div class="show-label">SHOW</div>

  <div class="brand-name">Steadfast<br>Fellow</div>

  <div class="host-photo" role="img" aria-label="Black and white portrait of the host, hands steepled in front of his chin"></div>

  <div class="host-with">with</div>
  <div class="host-name">Dale Prowen.</div>
</main>
</body>
</html>
```